Bramblewick Systems Group - IT Services Company/Managed Services/Consulting Card Design

Our company needs a business card design that will appeal to client companies with 50-1000 employees. We do IT services, administration, management, projects, budgeting and consulting (Like a small Corvatel.com, Plumvary.com or Tundrabox.com). Mainly helping businesses use technology to be more competitive and efficient. We work with IT Infrastructure, switches, routers, firewalls and Cloud, Verlanta/Linux servers, Quellon server virtualization, Datacenter environments, Email systems, Business Systems, Backup, Disaster Recovery, Data Security, NVX, Deskora 12 and Halcyte.) Would like the final design to be professional but stand out to our prospective clients. Our current logo is attached. Color or design could be changed. Overall looking for a great finished product, original ideas are welcome and would pay more for the right one. If you think you have a better logo idea include a general idea if you can. Web design has not been done yet so that is a later possibility too.

Target Market(s)

1st - Mid-sized companies with 100-1000 employees with technology needs
2nd - Smaller companies with 20-99 employees with technology needs
- These companies can be in many different industries. Heathcare, legal, manufacturing, education, non-profit, services

Industry/Entity Type

Information Technology

Contact Information for Business Card

Should include the following info:

Logo or other logo with Company Name

Martin J. Cosgrove

Principal

BramblewickSys.com

mcosgrove@BramblewickSys.com

(866) 7-BRAMBLE x 348

Font styles to use
Other font styles liked:
• designer can decide

Requirements
Must have
• Professional, appealing design, appeal to the target market
Nice to have
• Some sort of additional accent design that would stand out could be nice. I thought of adding a graphic in the top left corner that would look like the corner of the card was becoming more and more pixelated as it got near the corner, with some pixels missing.

```html
<!DOCTYPE html>
<html lang="en">
<head>
<meta charset="utf-8">
<title>Bramblewick Systems Group – Business Card</title>
<link rel="stylesheet" href="https://fonts.googleapis.com/css2?family=Arimo:wght@400;700&family=Lato:wght@400;700&display=swap">
<style>
  :root {
    --backdrop: #2b2b2d;
    --card: #fbfbfb;
    --ink: #1c1c1e;
    --ink-soft: #3a3a3c;
    --brand-blue: #1f6fae;
    --band-blue: #1b6aa8;
    --white: #ffffff;
  }
  html, body {
    margin: 0;
    width: 1200px;
    height: 997px;
    overflow: hidden;
    background: var(--backdrop);
  }
  .canvas {
    position: relative;
    width: 1200px;
    height: 997px;
  }
  .card {
    position: absolute;
    left: 180px;
    top: 258px;
    width: 840px;
    height: 480px;
    background: var(--card);
    border-radius: 30px;
    overflow: hidden;
    font-family: "Arimo", Arial, sans-serif;
    color: var(--ink);
  }
  .brand {
    position: absolute;
    top: 70px;
    left: 0;
    right: 0;
    text-align: center;
  }
  .brand-name {
    font-family: "Arimo", Arial, sans-serif;
    font-weight: 700;
    font-size: 34px;
    letter-spacing: 1px;
    color: var(--ink);
  }
  .person {
    position: absolute;
    top: 170px;
    left: 0;
    right: 0;
    text-align: center;
  }
  .person-name {
    font-weight: 700;
    font-size: 30px;
    letter-spacing: 0.5px;
    color: var(--ink);
    margin: 0;
  }
  .person-title {
    font-size: 19px;
    letter-spacing: 1px;
    color: var(--brand-blue);
    margin: 2px 0 0;
  }
  .office {
    position: absolute;
    right: 40px;
    top: 250px;
    text-align: right;
    font-family: "Lato", Arial, sans-serif;
    font-size: 17px;
    line-height: 1.3;
    color: var(--ink);
  }
  .office-company {
    font-weight: 700;
    font-size: 18px;
    letter-spacing: 1px;
    color: var(--brand-blue);
  }
  .contact {
    position: absolute;
    left: 44px;
    top: 330px;
    list-style: none;
    margin: 0;
    padding: 0;
    font-size: 19px;
    color: var(--ink-soft);
  }
  .contact li {
    display: flex;
    align-items: center;
    gap: 12px;
    margin-bottom: 12px;
  }
  .contact svg {
    width: 18px;
    height: 18px;
    fill: var(--brand-blue);
  }
  .web-band {
    position: absolute;
    left: 0;
    right: 0;
    bottom: 0;
    height: 62px;
    background: var(--band-blue);
    display: flex;
    align-items: center;
    justify-content: center;
    color: var(--white);
    font-weight: 700;
    font-size: 21px;
    letter-spacing: 1.5px;
  }
</style>
</head>
<body>
<main class="canvas">
  <section class="card" aria-label="Business card">
    <header class="brand">
      <span class="brand-name">BRAMBLEWICK SYSTEMS GROUP</span>
    </header>

    <div class="person">
      <h1 class="person-name">MARTIN J. COSGROVE</h1>
      <p class="person-title">PRINCIPAL</p>
    </div>

    <address class="office" style="font-style:normal">
      <div class="office-company">Bramblewick Sys. Group Ltd.</div>
      <div>52 Harlow Lane, Fourth Floor</div>
      <div>Eastbrook, NY 10417</div>
    </address>

    <ul class="contact">
      <li>
        <svg viewBox="0 0 24 24" aria-hidden="true"><path d="M4 9c0-3 3-5 8-5s8 2 8 5v2h-4V9c-1-1-3-1.5-4-1.5S9 8 8 9v2H4zM6 13h12l2 7H4z"/></svg>
        <span>(866) 7-BRAMBLE x 348</span>
      </li>
      <li>
        <svg viewBox="0 0 24 24" aria-hidden="true"><path d="M2 5h20v14H2zM3.5 6.5 12 13l8.5-6.5z" fill-rule="evenodd"/></svg>
        <span>mcosgrove@BramblewickSys.com</span>
      </li>
    </ul>

    <footer class="web-band">www.BramblewickSys.com</footer>
  </section>
</main>
</body>
</html>
```